Children Probiotics , Mom Probiotics

We need 2 package designs. One for children, One for mother
The design should be the same style as the other products. The design should be cartoon , lovely, cheerful. And same time , knowing the product is probiotics, to help children/mother‘s intestines and stomach
more health.

1.Kids Probiotics package box + Printed stick foil
2.Mom Probiotics package box + Printed stick foil

The Kids Probiotics has yellow-orange as the main colour
Mom Probiotics has pink.

```html
<!DOCTYPE html>
<html lang="en">
<head>
<meta charset="utf-8">
<title>Yippa Mom Probiotics – Packaging</title>
<link rel="stylesheet" href="https://fonts.googleapis.com/css2?family=Lilita+One&family=Fredoka:wght@500;600&family=Open+Sans:wght@400;600&family=Yellowtail&display=swap">
<style>
:root{
  --pink:#fbc2cb;
  --pink-light:#fde4e8;
  --red:#e1262f;
  --red-dark:#a52333;
  --band:#cf3e4b;
  --teal:#5cbcbf;
  --green:#6aae43;
  --ink:#7a2430;
  --paper:#ffffff;
}
*{margin:0;padding:0;box-sizing:border-box}
html,body{width:1200px;height:3051px;overflow:hidden;background:var(--paper)}
.sheet{position:relative;width:1024px;height:2603.5px;transform:scale(1.171875);transform-origin:0 0}

/* front face design, reused across box, foils and dielines */
.front{position:absolute;overflow:hidden;background:linear-gradient(var(--pink-light),var(--pink) 55%);font-size:10px;font-family:'Fredoka',sans-serif}
.front .brand{position:absolute;top:6%;width:100%;text-align:center;font-weight:600;font-size:1.7em;line-height:1;color:var(--teal);letter-spacing:.02em}
.front .title{position:absolute;top:17%;width:100%;text-align:center;font-family:'Lilita One',sans-serif;font-size:4.2em;line-height:1;color:var(--red)}
.front .subtitle{position:absolute;top:35%;width:100%;text-align:center;font-family:'Lilita One',sans-serif;font-size:1.75em;line-height:1;color:var(--red);letter-spacing:.02em}
.front .claims{position:absolute;top:45%;left:12%;right:4%;list-style:none;font-weight:500;font-size:.74em;line-height:1.55;white-space:nowrap;color:var(--teal)}
.claims li::before,.benefits li::before{content:"✓";color:var(--green);font-weight:700;margin-right:.35em}
.front .band{position:absolute;left:-10%;bottom:0;width:120%;height:19%;border-radius:50% 50% 0 0/30% 30% 0 0;background:linear-gradient(var(--band),var(--red-dark))}
.front .art{position:absolute;left:14%;top:59%;width:54%;height:34%;border-radius:46% 46% 40% 40%;background:radial-gradient(ellipse at 40% 40%,#ee4a52,#d42a36 55%,#b8243a)}
.front .taste{position:absolute;left:56%;top:56%;width:40%;text-align:center;font-family:'Yellowtail',cursive;font-size:1.6em;line-height:.95;color:var(--red);transform:rotate(-10deg)}
.front .cfu{position:absolute;right:6%;bottom:3.5%;font-family:'Lilita One',sans-serif;font-size:1.3em;line-height:1;color:var(--paper);letter-spacing:.04em}

/* flat box face */
.box-face{left:320px;top:140px;width:385px;height:470px;font-size:19.5px}

/* stick foils */
.foil-strip{position:absolute;left:85px;width:865px;height:228px;overflow:hidden;display:flex}
.foil-strip .front{position:relative;flex:0 0 198px;height:228px}
.foil-strip .front+.front{border-left:2px dashed var(--paper)}
.row-a{top:680px}
.row-b{top:945px}

/* dieline */
.dieline{position:absolute;left:0;width:1024px;height:625px}
.die-a{top:1215px}
.die-b{top:1890px}
.flap{position:absolute;background:var(--pink)}
.panel{position:absolute;top:195px;height:235px;overflow:hidden;background:linear-gradient(var(--pink-light),var(--pink) 55%);font-family:'Open Sans',sans-serif;font-size:6.8px;line-height:1.3;color:var(--ink)}
.panel .band{position:absolute;left:-10%;bottom:0;width:120%;height:17%;border-radius:50% 50% 0 0/30% 30% 0 0;background:linear-gradient(var(--band),var(--red-dark))}
.dieline .front{top:195px;left:478px;width:192px;height:235px;font-size:9.6px}

.lid{left:315px;top:3px;width:158px;height:192px}
.lid-mark{position:absolute;top:100px;width:100%;text-align:center}
.lid-mark .brand{font-family:'Fredoka',sans-serif;font-weight:600;font-size:13px;color:var(--teal)}
.lid-mark .title{font-family:'Lilita One',sans-serif;font-size:24px;line-height:1;color:var(--red)}
.lid-mark .subtitle{font-family:'Lilita One',sans-serif;font-size:11.5px;line-height:1;color:var(--red)}

.panel-back{left:117px;width:193px;padding:33px 16px 0 18px}
.panel-back h3,.panel-dose h3{font-family:'Lilita One',sans-serif;font-weight:400;font-size:8px;color:var(--red);margin:8px 0 2px}
.benefits{list-style:none;margin-top:2px}
.benefits li{padding-left:8px;text-indent:-8px}
.badges{position:absolute;left:18px;bottom:8px;display:flex;gap:6px;z-index:1}
.badge{width:18px;height:18px;border-radius:50%;background:var(--paper);opacity:.85}
.badge.square{border-radius:3px;width:22px}

.panel-side{left:310px;width:168px;padding:70px 14px 0 14px}
.panel-side .brand{font-family:'Fredoka',sans-serif;font-weight:600;font-size:20px;line-height:1;color:var(--teal);margin-bottom:10px}
.panel-side .maker{position:absolute;left:14px;bottom:10px;z-index:1;color:var(--paper)}
.panel-side .fruit{position:absolute;left:110px;top:160px;width:40px;height:32px;border-radius:50% 50% 45% 45%;background:radial-gradient(ellipse at 40% 40%,#ee4a52,#b3202c)}

.panel-dose{left:670px;width:165px;padding:10px 10px 0 12px}
.panel-dose h3{margin-top:6px}
.panel-dose .dose{color:var(--teal);margin-bottom:4px}
.nutrition{width:100%;border-collapse:separate;border-spacing:0 2px;margin-top:4px;font-size:6px;line-height:1.2}
.nutrition th{background:var(--red-dark);color:var(--paper);font-weight:600;text-align:left;padding:2px 4px}
.nutrition th:last-child,.nutrition td:last-child{text-align:right;white-space:nowrap}
.nutrition td{background:#f3a6b1;padding:2px 4px;vertical-align:top}
.ingredients{position:absolute;left:12px;right:8px;bottom:4px;z-index:1;color:var(--paper);font-size:5.4px;line-height:1.2}
.ingredients h4{font-family:'Lilita One',sans-serif;font-weight:400;font-size:6.5px}
.panel-dose .band{height:25%}

.glue{left:835px;top:203px;width:40px;height:220px}
</style>
</head>
<body>
<div class="sheet">

  <!-- box front, flat -->
  <div class="front box-face">
    <div class="brand">Yippa</div>
    <div class="title">MOM</div>
    <div class="subtitle">PROBIOTICS</div>
    <ul class="claims"><li>Support a healthy digestive system</li><li>Maintain balance of the microbiota</li></ul>
    <div class="band"></div>
    <div class="art" role="img" aria-label="Illustration of a strawberry and a raspberry splashing in berry juice"></div>
    <div class="taste">Redberry<br>Taste</div>
    <div class="cfu">120 CFU</div>
  </div>

  <!-- stick foils -->
  <div class="foil-strip row-a">
    <div class="front"><div class="brand">Yippa</div><div class="title">MOM</div><div class="subtitle">PROBIOTICS</div><ul class="claims"><li>Support a healthy digestive system</li><li>Maintain balance of the microbiota</li></ul><div class="band"></div><div class="art" role="img" aria-label="Strawberry and raspberry illustration"></div><div class="taste">Redberry<br>Taste</div><div class="cfu">120 CFU</div></div>
    <div class="front"><div class="brand">Yippa</div><div class="title">MOM</div><div class="subtitle">PROBIOTICS</div><ul class="claims"><li>Support a healthy digestive system</li><li>Maintain balance of the microbiota</li></ul><div class="band"></div><div class="art" role="img" aria-label="Strawberry and raspberry illustration"></div><div class="taste">Redberry<br>Taste</div><div class="cfu">120 CFU</div></div>
    <div class="front"><div class="brand">Yippa</div><div class="title">MOM</div><div class="subtitle">PROBIOTICS</div><ul class="claims"><li>Support a healthy digestive system</li><li>Maintain balance of the microbiota</li></ul><div class="band"></div><div class="art" role="img" aria-label="Strawberry and raspberry illustration"></div><div class="taste">Redberry<br>Taste</div><div class="cfu">120 CFU</div></div>
    <div class="front"><div class="brand">Yippa</div><div class="title">MOM</div><div class="subtitle">PROBIOTICS</div><ul class="claims"><li>Support a healthy digestive system</li><li>Maintain balance of the microbiota</li></ul><div class="band"></div><div class="art" role="img" aria-label="Strawberry and raspberry illustration"></div><div class="taste">Redberry<br>Taste</div><div class="cfu">120 CFU</div></div>
    <div class="front"><div class="brand">Yippa</div><div class="title">MOM</div><div class="subtitle">PROBIOTICS</div><ul class="claims"><li>Support a healthy digestive system</li><li>Maintain balance of the microbiota</li></ul><div class="band"></div><div class="art" role="img" aria-label="Strawberry and raspberry illustration"></div><div class="taste">Redberry<br>Taste</div><div class="cfu">120 CFU</div></div>
  </div>

  <div class="foil-strip row-b">
    <div class="front"><div class="brand">Yippa</div><div class="title">MOM</div><div class="subtitle">PROBIOTICS</div><ul class="claims"><li>Support a healthy digestive system</li><li>Maintain balance of the microbiota</li></ul><div class="band"></div><div class="art" role="img" aria-label="Strawberry and raspberry illustration"></div><div class="taste">Redberry<br>Taste</div><div class="cfu">120 CFU</div></div>
    <div class="front"><div class="brand">Yippa</div><div class="title">MOM</div><div class="subtitle">PROBIOTICS</div><ul class="claims"><li>Support a healthy digestive system</li><li>Maintain balance of the microbiota</li></ul><div class="band"></div><div class="art" role="img" aria-label="Strawberry and raspberry illustration"></div><div class="taste">Redberry<br>Taste</div><div class="cfu">120 CFU</div></div>
    <div class="front"><div class="brand">Yippa</div><div class="title">MOM</div><div class="subtitle">PROBIOTICS</div><ul class="claims"><li>Support a healthy digestive system</li><li>Maintain balance of the microbiota</li></ul><div class="band"></div><div class="art" role="img" aria-label="Strawberry and raspberry illustration"></div><div class="taste">Redberry<br>Taste</div><div class="cfu">120 CFU</div></div>
    <div class="front"><div class="brand">Yippa</div><div class="title">MOM</div><div class="subtitle">PROBIOTICS</div><ul class="claims"><li>Support a healthy digestive system</li><li>Maintain balance of the microbiota</li></ul><div class="band"></div><div class="art" role="img" aria-label="Strawberry and raspberry illustration"></div><div class="taste">Redberry<br>Taste</div><div class="cfu">120 CFU</div></div>
    <div class="front"><div class="brand">Yippa</div><div class="title">MOM</div><div class="subtitle">PROBIOTICS</div><ul class="claims"><li>Support a healthy digestive system</li><li>Maintain balance of the microbiota</li></ul><div class="band"></div><div class="art" role="img" aria-label="Strawberry and raspberry illustration"></div><div class="taste">Redberry<br>Taste</div><div class="cfu">120 CFU</div></div>
  </div>

  <!-- box dieline A -->
  <div class="dieline die-a">
    <div class="flap lid"><div class="lid-mark"><div class="brand">Yippa</div><div class="title">MOM</div><div class="subtitle">PROBIOTICS</div></div></div>
    <div class="flap" style="left:683px;top:50px;width:145px;height:145px"></div>
    <div class="flap" style="left:124px;top:147px;width:181px;height:48px"></div>
    <div class="flap" style="left:481px;top:147px;width:184px;height:48px"></div>

    <div class="panel panel-back">
      <p>Probiotic bacteria are 'live microorganism that when administered in adequate amounts can provide a benefit to the host' according to WHO.</p>
      <h3>MOM AND BABY</h3>
      <p>Supports general health of the pregnant woman and the baby during pregnancy.</p>
      <p>Clinical studies showing:</p>
      <ul class="benefits"><li>Reduced risk of preterm delivery</li><li>Reduced risk of gestational diabetes</li><li>Reduced risk of the baby developing atopic dermatitis</li></ul>
      <div class="band"></div>
      <div class="badges"><span class="badge"></span><span class="badge"></span><span class="badge"></span><span class="badge square"></span></div>
    </div>

    <div class="panel panel-side">
      <div class="brand">Yippa</div>
      <p>Kosttilskudd erstatter ikke et variert kosthold.<br>Anbefalt døgndose bør ikke overskrides.<br>Oppbevares utilgjengelig for barn.<br>Produsert i Denmark</p>
      <div class="fruit" role="img" aria-label="Small strawberry illustration"></div>
      <div class="band"></div>
      <p class="maker">Yippa AS ,Norge<br>www.yippago.example</p>
    </div>

    <div class="front"><div class="brand">Yippa</div><div class="title">MOM</div><div class="subtitle">PROBIOTICS</div><ul class="claims"><li>Support a healthy digestive system</li><li>Maintain balance of the microbiota</li></ul><div class="band"></div><div class="art" role="img" aria-label="Strawberry and raspberry illustration"></div><div class="taste">Redberry<br>Taste</div><div class="cfu">120 CFU</div></div>

    <div class="panel panel-dose">
      <h3>ANBEFALT DOGNDOSE:</h3>
      <p class="dose">1 stick per day</p>
      <p>Pour the powder directly into the mouth. Dissolves instantly on the tongue. No need for water.</p>
      <table class="nutrition">
        <tr><th>Innhold</th><th>1 stick</th></tr>
        <tr><td>Bifidobacterium animalis ssp lactis PROLAC™12</td><td>21.3 CFU</td></tr>
        <tr><td>Lactobacillus acidophilus PROLAC™5</td><td>50 CFU</td></tr>
        <tr><td>Lactobacillus rhamnosus PROLAC™GG</td><td>48 CFU</td></tr>
      </table>
      <div class="band"></div>
      <div class="ingredients"><h4>INGREDIENSER</h4>Erythritol, Xylitol, Mono- and diglycerides of fatty acids, Magnesium oxide, Citric acid, Sodium carboxymethylcellulose, Silicon dioxide, Magnesium salts of fatty acids, Strawberry flavour, Raspberry flavour.</div>
    </div>

    <div class="flap glue"></div>
    <div class="flap" style="left:315px;top:430px;width:158px;height:190px"></div>
    <div class="flap" style="left:683px;top:430px;width:145px;height:145px"></div>
    <div class="flap" style="left:124px;top:430px;width:181px;height:45px"></div>
    <div class="flap" style="left:481px;top:430px;width:184px;height:45px"></div>
  </div>

  <!-- box dieline B -->
  <div class="dieline die-b">
    <div class="flap lid"><div class="lid-mark"><div class="brand">Yippa</div><div class="title">MOM</div><div class="subtitle">PROBIOTICS</div></div></div>
    <div class="flap" style="left:683px;top:50px;width:145px;height:145px"></div>
    <div class="flap" style="left:124px;top:147px;width:181px;height:48px"></div>
    <div class="flap" style="left:481px;top:147px;width:184px;height:48px"></div>

    <div class="panel panel-back">
      <p>Probiotic bacteria are 'live microorganism that when administered in adequate amounts can provide a benefit to the host' according to WHO.</p>
      <h3>MOM AND BABY</h3>
      <p>Supports general health of the pregnant woman and the baby during pregnancy.</p>
      <p>Clinical studies showing:</p>
      <ul class="benefits"><li>Reduced risk of preterm delivery</li><li>Reduced risk of gestational diabetes</li><li>Reduced risk of the baby developing atopic dermatitis</li></ul>
      <div class="band"></div>
      <div class="badges"><span class="badge"></span><span class="badge"></span><span class="badge"></span><span class="badge square"></span></div>
    </div>

    <div class="panel panel-side">
      <div class="brand">Yippa</div>
      <p>Kosttilskudd erstatter ikke et variert kosthold.<br>Anbefalt døgndose bør ikke overskrides.<br>Oppbevares utilgjengelig for barn.<br>Produsert i Denmark</p>
      <div class="fruit" role="img" aria-label="Small strawberry illustration"></div>
      <div class="band"></div>
      <p class="maker">Yippa AS ,Norge<br>www.yippago.example</p>
    </div>

    <div class="front"><div class="brand">Yippa</div><div class="title">MOM</div><div class="subtitle">PROBIOTICS</div><ul class="claims"><li>Support a healthy digestive system</li><li>Maintain balance of the microbiota</li></ul><div class="band"></div><div class="art" role="img" aria-label="Strawberry and raspberry illustration"></div><div class="taste">Redberry<br>Taste</div><div class="cfu">120 CFU</div></div>

    <div class="panel panel-dose">
      <h3>ANBEFALT DOGNDOSE:</h3>
      <p class="dose">1 stick per day</p>
      <p>Pour the powder directly into the mouth. Dissolves instantly on the tongue. No need for water.</p>
      <table class="nutrition">
        <tr><th>Innhold</th><th>1 stick</th></tr>
        <tr><td>Bifidobacterium animalis ssp lactis PROLAC™12</td><td>21.3 CFU</td></tr>
        <tr><td>Lactobacillus acidophilus PROLAC™5</td><td>50 CFU</td></tr>
        <tr><td>Lactobacillus rhamnosus PROLAC™GG</td><td>48 CFU</td></tr>
      </table>
      <div class="band"></div>
      <div class="ingredients"><h4>INGREDIENSER</h4>Erythritol, Xylitol, Mono- and diglycerides of fatty acids, Magnesium oxide, Citric acid, Sodium carboxymethylcellulose, Silicon dioxide, Magnesium salts of fatty acids, Strawberry flavour, Raspberry flavour.</div>
    </div>

    <div class="flap glue"></div>
    <div class="flap" style="left:315px;top:430px;width:158px;height:190px"></div>
    <div class="flap" style="left:683px;top:430px;width:145px;height:145px"></div>
    <div class="flap" style="left:124px;top:430px;width:181px;height:45px"></div>
    <div class="flap" style="left:481px;top:430px;width:184px;height:45px"></div>
  </div>

</div>
</body>
</html>
```